RESTAURANT MENU

WANTING TO CHANGE MENU DESIGN AND ADD SOME PLATES AND DESSERTS

ILL POST PICTURES OF LOGO AND PLATES. DONT HAVE ANYTHING IN MIND JUST NEED SOMETHING NEW THAT WILL STAND OUT .

Industry/Entity Type

Restaurant

Requirements
Must have
• THE SIZE RIGHT NOW IS 11X17 TRIFOLD MENU.
• IF ITS TOO CROWDED WITH THE NEW PLATES I DONT MIND MAKING IT BIGGER .
• ADD ONS
• ******************************** PASTAS **************************
• CHICKEN FETTUCCINE OR PENNE PASTA - 9.25
• SHRIMP FETTUCCINE OR PENNE PAST 10.25
• ******************* WINGS ***************************************
• BONELESS OR TRADITIONAL
• 5 WINGS - 5.99
• 10 WINGS - 8.99
• 20 WINGS - 14.99
• 50 WINGS - 35.99
• mild , hot , lemon pepper , sweet chili , teriyaki , garlic Parmesan
• *****************FROM THE BAR-B-QUE*************
• BABY BACK RIBS
• half rack - 12.99
• full rack - 18.99
• BRISKET BURGER 8.25
• BARBECUE COMBO - 17.99
• half rack of ribs, brisket , and sausage
• served with potato salad and red beans.
Should not have
• ADRESS CORRECTION ****
• 718 N. CALLOWAY ST.
• ELSA TEXAS
• ************* APPETIZERS***********
• Jalapeno cheese fries ............................. 4.99
• Mozzarella cheese sticks ........................ 5.25
• Classic Nachos ( ground bee) ................. 6.99
• Nachos ( fajita or chicken fajita ).............. 7.99
• Panchos ....................................................8.99
• ( includes lettuce , and avocado )
• Shrimp Nachos ........................................8.99
• Choriqueso...............................................6.99
• Guacamole ..............................................5.99
• ***************SALADS******************
• House Salad ...........................................5.99
• Caesar Salad...........................................5.99
• Chef Salad ...............................................7.99
• Grilled or Crispy chicken Salad ................8.99
• Shrimp Salad ............................................9.99
• ***************BURGERS AND SANDWICHES ****************
• Fajita Steak Burger .............................................................8.95
• (fine cut fajita loaded with fresh sauteed mushrooms , and topped with
• mozzarella cheese, crisp lettuce , onions , tomatoes mayo & mustard)
• Mushroom Swiss Burger .....................................................8.95
• (loaded with fresh saureed mushrooms, and topped with melted Swiss cheese)
• Hawaiian Burger ..................................................................7.99
• (topped with pineapple , american cheese , crisp lettuce , tomatoes and mayo. )
• Barbecue Burger.......................................................................7.99
• (basted with our original Bbq sauce, American cheese , lettuce , fresh tomatoes , mayo and mustard.)
• Patty Melt ................................................................................7.99
• Cheese Burger ........................................................................6.99
• Double Cheese Burger............................................................7.99
• Grilled or Fried Chicken Burger ................................................6.99
• Fish Burger ..............................................................................6.99
• (breaded fish with lettuce, tomatoes & tartar sauce )
• Blt..................................................................................4.99
• (bacon , lettuce & tomato sandwich )
• *******all burgers are served with french fries ***************
• *******ADD THREE SLICES OF BACON TO ANY BURGER ******
• ..................................1.25.
• **************KIDS MENU *****************
• Hamburger combo ..................................3.50
• cheese burger combo ..............................3.99
• Grilled ham and cheese ...........................3.50
• Chicken Tenders .......................................3.99
• Enchilada plate .........................................3.99
• (two enchiladas , rice & beans )
• Ground Beef tacos ...................................3.99
• (2 crispy or soft ground beef tacos , lettuce and cheese )
• ***************SPECIALTIES ***********************
• Chile Relleno ......................................................9.99
• (ground beef or cheese )
• Shrimp and cheese Chile Relleno ......................10.99
• Hamburger steak .................................................8.99
• 8 oz Grilled Chicken Breast .................................8.99
• Chicken Fried Chicken ........................................8.99
• Chicken Fried Steak .............................................8.99
• T Bone .................................................................12.99
• Pork Chops ..........................................................8.99
• Arrachera Steak ...................................................9.99
• ****************COMBINATION PLATES***********************
• Lurma's Special ..................................................8.99
• (fajita with two enchiladas on the side , rice and beans )
• Tampiquena .........................................................9.99
• (fajita steak with two enchiladas on the side , rice and beans
• Rio Bravo Plate .....................................................11.99
• (1 beef or cheese chile relleno with fajita steak on the side , rice and beans )
• Fajita & Shrimp plate .............................................11.99
• T Bone & Shrimp ......................................................13.99
• ************SOUTH OF THE BORDER ****************
• Cheese Enchiladaas ..................................................7.99
• Beef or Chicken Enchiladas ......................................8.99
• Mexican Plate .............................................................9.50
• (three enchiladas , one ground beef taco, and one chicken chalupa )
• Bean and Cheese Chalupa...........................................7.99
• Beef or Chicken Chalupas............................................8.99
• Chicken Flautas ..........................................................8.99
• Beef Milanesa .............................................................8.99
• Chicken Milanesa..........................................................8.99
• Bisteck Ranchero ..........................................................8.99
• Fajita or Chicken plate ...................................................8.99
• Fajita Toreada ................................................................8.99
• Pechuga Santa Fe.........................................................8.99
• Carne Guisada Plate......................................................8.99
• Fajita or Chicken Quesadillas .......................................9.99
• Shrimp Quesadillas ......................................................10.99
• Fajita or Chicken Tacos .................................................8.99
• Ground Beef tacos ( crispy or soft )...............................7.99
• **all Plates are served with rice and beans ***
• ****************TACOS ************
• Chicken fajita taco .....................................2.99
• Fajita taco ..................................................2.99
• Carne guisada ..........................................2.99
• Ground Beef taco ......................................2.50
• ************SOUPS ******************
• Caldo de Res ..........................small 6.99.................large....7.99
• Caldo de Pescado y Camaron ..small 7.99..............large ....8.99
• Caldo Siete Mares .....................small 8.99.............large ....9.99
• Menudo ....................................small ..6.99.............large ..7.99
• Caldo Tlalpeno ..........................small .. 7.99........large 8.99
• *********SEAFOOD*************
• Fish Tacos .................................................8.99
• (fish filet on corn tortilla , rice on the side )
• Fish Plate (Grilled or Fried ).........................11.99
• Shrimp Plate (any style)................................12.99
• (al mojo de ajo, ala diabla, agua chiles , fried)
• Costa Azul ....................................................14.99
• ( 6 shrimp wrapped in bacon and breaded to perfection , filled with mozzarella cheese , served with fries , rice and salad )
• Seafood Fiesta .............................................14.99
• ( combination of fish , shrimp and crab)
• Shrimp Cocktail .......................................small ..9.99.....large...12.99
• ***********FAMILY PLATTERS **************************
• Botana or Sombrero for 1 .............................................10.99
• Botana or Sombrero for 2 ..............................................20.99
• Botana or Sombrero for 3 ..............................................27.99
• Botana or Sombrero for 4 ..............................................38.99
• Botana or Sombrero for 6................................................49.99
• (beef chicken or mixed )
• Seafood platter for 2 ........................................................25.99
• Seafood platter for 3 ........................................................33.99
• Seafood platter for 4 ........................................................44.99
• Seafood platter for 6.........................................................59.99
• Mar y Tierra for 2 ............................................................26.99
• Mar y Tierra for 3 ............................................................35.99
• Mar y Tierra for 4 .............................................................43.99
• Mar y Tierra for 6...............................................................58.99
• *********BREAKFAST PLATES *************************
• Potato & Egg Plate ...................................4.99
• Bacon & Egg Plate ....................................4.99
• Migas & Egg Plate.....................................4.99
• Huevos Rancheros ...................................4.99
• Huevo ala Mexicana ..................................4.99
• Chorizo & Egg Plate ..................................4.99
• Sausage & Egg Plate ................................4.99
• Ham & Egg Plate........................................4.99
• Machacado & Egg Plate ............................5.99
• Chicharron en Salsa.....................................5.99
• Chicharron & Egg Plate................................5.99
• Chicharron en salsa with 2 eggs ..................6.99
• Chilaquiles .................................................5.99
• Huevos Divorciados ...................................6.99
• Chicken Chilaquiles ..................................6.99
• Fajita Asada & egg ......................................7.99
• Barbacoa Plate ............................................6.99
• ( add two eggs )............................................7.99
• **************GOURMET BREAKFAST*****
• Lurma's Favorite .............................................7.99
• two eggs , one slice of ham , two bacon , two sausage links and two buttermilk pancakes
• Lurma's Special ..........................................................3.99
• Two eggs , sausage , ham or bacon
• Ham and cheese Omelette .......................................6.99
• three egg omelette filled with ham and cheese , hash-brown and toast.
• Ultimate Omelette ....................................................7.99
• Three egg omelette with sausage , bacon , fire roasted bell peppers and onion , mushrooms , diced tomatoes and shredded cheese . served with hash-browns and toast .
• Meat lovers Omelette ......................................................8.99
• Three egg omelette with grilled steak , fire roasted bell peppers and onions.
• sauteed mushrooms and melted mozzarella cheese.
• The steakwich ...............................................7.99
• two scrambled eggs, tender steak , american cheese on texas toast .
• Hamwich .......................................................5.99
• sausagewich .................................................5.99
• Chicken Fried steak and eggs .......................7.99
• Pork chops and Eggs .....................................9.99
• T Bone Steak and eggs ...............................10.99
• **********BREAKFAST TACOS ********************
• Bacon & egg ...................1.99
• Sausage & Egg ................1.99
• Potato & Egg...................1.99
• Chorizo & Egg .................1.99
• Bean &Egg.......................1.99
• Ham and Egg ....................1.99
• Machacado & Egg ............2.59
• Chicharron & Egg .............2.59
• Gorditas .............................2.99
• *****extra taco filling *** .35
• *********DRINKS ***********
• Coffee..............................1.99
• Milk ..................................1.99
• Orange Juice ...................2.50
• (no refill )
• Sweet & unsweet Tea ..........2.15
• Raspberry Tea ...................2.50
• Fountain Drinks ..................2.15
• Strawberry lemonade ...........2.50
• Lemonade .............................2.50
• hot chocolate ...........................1.99
• *****15% WILL BE ADDED ON TABLES OF 6 OR MORE ***

```html
<!DOCTYPE html>
<html lang="en">
<head>
<meta charset="utf-8">
<title>Lurma's — Food and Drink Menu</title>
<link rel="stylesheet" href="https://fonts.googleapis.com/css2?family=Cabin+Condensed:wght@400;500&family=Fredoka:wght@500;600&family=Raleway:wght@400;600;700&display=swap">
<style>
  :root {
    --page: #ece7e0;
    --green: #2f4a2b;
    --olive: #4a4a26;
    --rust: #7a3418;
    --brown: #4a2c17;
    --brown-deep: #3a2212;
    --band: #231f1d;
    --orange: #f08a1c;
    --orange-deep: #e0601a;
    --yellow: #f7e35a;
    --ink: #f4efe6;
    --dark: #2a1a10;
    --plate: #d8c9a4;
  }
  * { box-sizing: border-box; margin: 0; padding: 0; }
  html, body { width: 1200px; height: 1200px; overflow: hidden; background: var(--page); }
  .menu {
    position: absolute; left: 20px; top: 226px;
    width: 1300px; height: 838px;
    transform: scale(0.8923); transform-origin: 0 0;
    display: flex; box-shadow: 0 6px 18px rgba(0,0,0,.35);
    font-family: "Cabin Condensed", sans-serif; color: var(--ink);
  }
  .panel { position: relative; width: 433px; height: 100%; overflow: hidden; }
  .panel--inside { background: linear-gradient(180deg, var(--green) 0%, var(--olive) 50%, var(--rust) 100%); }
  .panel--middle { width: 434px; border-left: 1px solid rgba(0,0,0,.25); }
  .panel--cover { width: 433px; background: linear-gradient(160deg, var(--rust) 0%, var(--brown) 22%, var(--brown-deep) 100%); border-left: 2px solid rgba(0,0,0,.35); }
  .footer-band {
    position: absolute; left: 0; right: 0; bottom: 0; height: 50px;
    background: var(--band); display: flex; align-items: center; justify-content: center;
    font-family: "Raleway", sans-serif;
  }
  .tag {
    position: absolute; display: inline-block; padding: 4px 12px 3px;
    background: linear-gradient(90deg, var(--orange-deep), var(--orange) 55%, #f7b52a);
    color: var(--dark); font-family: "Fredoka", sans-serif; font-weight: 600;
    font-size: 15px; letter-spacing: 1px; box-shadow: 2px 2px 0 rgba(0,0,0,.25);
  }
  .tag::after { content: ""; position: absolute; right: 0; top: 0; border-style: solid; border-width: 0 9px 9px 0; border-color: transparent rgba(255,255,255,.55) transparent transparent; }
  .list { position: absolute; font-size: 10.5px; line-height: 12.8px; }
  .row { display: flex; align-items: baseline; }
  .row .name { white-space: nowrap; }
  .row .dots { flex: 1; border-bottom: 1px dotted rgba(244,239,230,.6); margin: 0 1px; transform: translateY(-2px); }
  .row .price { white-space: nowrap; }
  .desc { display: block; white-space: nowrap; }
  .item { margin-bottom: 6.2px; }
  .photo { position: absolute; border-radius: 50%; border: 6px solid var(--orange); background: radial-gradient(circle at 50% 50%, #a67a3e 0%, #7b5a2e 35%, #c9b686 62%, var(--plate) 75%); }
  .center { text-align: center; }
</style>
</head>
<body>
<main class="menu">

  <!-- Breakfast plates -->
  <section class="panel panel--inside">
    <h2 class="tag" style="left:20px;top:22px;">BREAKFAST PLATES</h2>
    <div class="photo" role="img" aria-label="Breakfast plate with fajita meat, rice, avocado and a folded tortilla" style="left:-62px;top:282px;width:250px;height:246px;"></div>
    <div class="list" style="left:35px;top:64px;width:362px;">
      <div class="item"><div class="row"><span class="name">Potatoe &amp; Egg, Migas Plate</span><span class="dots"></span><span class="price">4.99</span></div><span class="desc">Bacon &amp; Egg , Huevos Rancheros, Huevo Ala Mexicana, Chorizo &amp; Egg,sausage<br>&amp; Egg, Ham &amp; Egg Comes With Beans , Potatoes And Tortillas</span></div>
      <div class="item"><div class="row"><span class="name">Side Orders</span><span class="dots"></span><span class="price">1.99</span></div><span class="desc">Egg, Sausage, Bacon, Ham, Hashbrown, Toast, Beans, Tortillas</span></div>
      <div class="item"><div class="row"><span class="name">Machacado Plate</span><span class="dots"></span><span class="price">5.99</span></div></div>
      <div class="item"><div class="row"><span class="name">Chicharron En Salsa</span><span class="dots"></span><span class="price">5.99</span></div></div>
      <div class="item"><div class="row"><span class="name">Chicharron &amp; Egg</span><span class="dots"></span><span class="price">5.99</span></div></div>
      <div class="item"><div class="row"><span class="name">Chicarron En Salsa With Two Eggs On Side</span><span class="dots"></span><span class="price">6.99</span></div></div>
      <div class="item"><div class="row"><span class="name">Chilaquiles</span><span class="dots"></span><span class="price">5.99</span></div></div>
      <div class="item"><div class="row"><span class="name">Huevos Divorciados</span><span class="dots"></span><span class="price">6.99</span></div></div>
      <div class="item"><div class="row"><span class="name">Chicken Chilaquiles</span><span class="dots"></span><span class="price">6.99</span></div></div>
      <div class="item" style="margin-left:52px;"><div class="row"><span class="name">Fajita Asada &amp; Egg</span><span class="dots"></span><span class="price">7.99</span></div></div>
      <div class="item" style="margin-left:96px;"><div class="row"><span class="name">Barbacoa Plate With Two Eggs</span><span class="dots"></span><span class="price">7.99</span></div><span class="desc" style="margin-left:20px;">Comes With Beans , Potatoes &amp; Tortillas</span></div>
      <div class="item" style="margin-left:141px;"><div class="row"><span class="name">Lurma's Favorite</span><span class="dots"></span><span class="price">7.99</span></div><span class="desc" style="margin-left:14px;">Two Eggs, One Slice Of Ham, two Bacon ,<br>&nbsp;&nbsp;Two Sasage Links And Two Buttermilk<br>&nbsp;&nbsp;&nbsp;&nbsp;Pancakes</span></div>
      <div class="item" style="margin-left:181px;"><div class="row"><span class="name">Lurma's Special</span><span class="dots"></span><span class="price">3.99</span></div><span class="desc" style="margin-left:4px;">Two Eggs , Sausage ,ham Or Bacon</span></div>
      <div class="item" style="margin-left:187px;"><div class="row"><span class="name">Ham And Cheese Omelette</span><span class="dots"></span><span class="price">6.99</span></div><span class="desc">Three Egg Omelette Filled With<br>Ham And Cheese , Hashbrowns And<br>Toast</span></div>
      <div class="item" style="margin-left:100px;"><div class="row" style="margin-left:74px;"><span class="name">Ultimate Omelette</span><span class="dots"></span><span class="price">7.99</span></div><span class="desc center">Three-egg Omelette With Sausage,<br>Bacon, Fire-roasted Peppers And Onions,<br>Mushrooms, Diced Tomatoes And Shredded<br>Cheddar Cheese. Served With Hash Browns And Toast.</span></div>
      <div class="item"><div class="row"><span class="name">Meat Lover Omelette</span><span class="dots"></span><span class="price">8.99</span></div><span class="desc">Three-egg Omelette With Grilled Steak, Fire-roasted Peppers And Onions,<br>Sautéed Mushrooms And Melted Monzerella Cheese.</span></div>
      <div class="item"><div class="row"><span class="name">The Steakwich</span><span class="dots"></span><span class="price">7.99</span></div><span class="desc">Two Scrambled Eggs, Tender Steak , American Cheese On A Texas Toast .<br>Served With Crispy Hash Browns.</span></div>
      <div class="item"><div class="row"><span class="name">Hamwich</span><span class="dots"></span><span class="price">5.99</span></div></div>
      <div class="item"><div class="row"><span class="name">Sausagewich</span><span class="dots"></span><span class="price">5.99</span></div></div>
      <div class="item"><div class="row"><span class="name">Chicken Fried Steak And Eggs</span><span class="dots"></span><span class="price">7.99</span></div><span class="desc">A Golden-fried Beef Steak Smothered In Rich Country Gravy. Served With<br>Two Eggs, Hash Browns And Toast</span></div>
      <div class="item"><div class="row"><span class="name">Pork Chop And Eggs</span><span class="dots"></span><span class="price">9.99</span></div></div>
      <div class="item"><div class="row"><span class="name">T-bone Steak And Eggs</span><span class="dots"></span><span class="price">10.99</span></div><span class="desc">A Tender . Seasoned T-bone Steak Served With Two Eggs, Hash Browns And<br>Toast .</span></div>
    </div>
    <footer class="footer-band"><span style="font-size:19px;">www.lurmasrestaurant.com</span></footer>
  </section>

  <!-- Tacos, drinks, pastas, wings, bbq -->
  <section class="panel panel--inside panel--middle">
    <div class="photo" role="img" aria-label="Plate with rice, beans, guacamole and a chile relleno" style="left:246px;top:2px;width:250px;height:220px;"></div>
    <h2 class="tag" style="left:20px;top:20px;">BREAKFAST TACOS</h2>
    <div class="list" style="left:35px;top:65px;width:175px;">
      <div class="row"><span class="name">Bacon &amp; Egg</span><span class="dots"></span><span class="price">1.99</span></div>
      <div class="row"><span class="name">Sausage &amp; Egg</span><span class="dots"></span><span class="price">1.99</span></div>
      <div class="row"><span class="name">Potatoe &amp; Egg</span><span class="dots"></span><span class="price">1.99</span></div>
      <div class="row"><span class="name">Chorizo &amp; Egg</span><span class="dots"></span><span class="price">1.99</span></div>
      <div class="row"><span class="name">Bean &amp; Egg</span><span class="dots"></span><span class="price">1.99</span></div>
      <div class="row"><span class="name">Ham &amp; Egg</span><span class="dots"></span><span class="price">1.99</span></div>
      <div class="row"><span class="name">Machacado &amp; Egg</span><span class="dots"></span><span class="price">2.59</span></div>
      <div class="row"><span class="name">Chicharron &amp; Egg</span><span class="dots"></span><span class="price">2.59</span></div>
      <div class="row"><span class="name">Chicharron En Salsa</span><span class="dots"></span><span class="price">2.59</span></div>
      <div class="row"><span class="name">Gorditas</span><span class="dots"></span><span class="price">2.99</span></div>
      <div>Extra Taco Filling .25</div>
    </div>

    <h2 class="tag" style="left:175px;top:212px;">DRINKS</h2>
    <div class="list" style="left:35px;top:253px;width:362px;">
      <div class="row"><span class="name">Cofee</span><span class="dots"></span><span class="price">1.99</span></div>
      <div class="row"><span class="name">Milk</span><span class="dots"></span><span class="price">1.99</span></div>
      <div class="row"><span class="name">Orange Juice (No Refill)</span><span class="dots"></span><span class="price">2.50</span></div>
      <div class="row"><span class="name">Sweet &amp; Unsweet Tea</span><span class="dots"></span><span class="price">2.15</span></div>
      <div class="row"><span class="name">Raspberry Tea</span><span class="dots"></span><span class="price">2.50</span></div>
      <div class="row"><span class="name">Fountain Drinks</span><span class="dots"></span><span class="price">2.15</span></div>
      <div class="row"><span class="name">Strawberry Lemonade</span><span class="dots"></span><span class="price">2.99</span></div>
      <div class="row"><span class="name">Lemonade</span><span class="dots"></span><span class="price">2.50</span></div>
      <div class="row"><span class="name">Hot Chocolate</span><span class="dots"></span><span class="price">1.99</span></div>
      <div class="row"><span class="name">Gorditas</span><span class="dots"></span><span class="price">2.99</span></div>
    </div>

    <h2 class="tag" style="left:175px;top:391px;">PASTAS</h2>
    <div class="list" style="left:35px;top:434px;width:362px;">
      <div class="row"><span class="name">CHICKEN FETTUCCINE OR PENNE PASTA</span><span class="dots"></span><span class="price">9.25</span></div>
      <div class="row"><span class="name">SHRIMP FETTUCCINE OR PENNE PAST</span><span class="dots"></span><span class="price">10.25</span></div>
    </div>

    <h2 class="tag" style="left:175px;top:478px;">WINGS</h2>
    <div class="list" style="left:35px;top:519px;width:362px;">
      <div class="center" style="margin-bottom:2px;">BONELESS OR TRADITIONAL</div>
      <div class="row"><span class="name">5 WINGS</span><span class="dots"></span><span class="price">5.99</span></div>
      <div class="row"><span class="name">10 WINGS</span><span class="dots"></span><span class="price">8.99</span></div>
      <div class="row"><span class="name">20 WINGS</span><span class="dots"></span><span class="price">14.99</span></div>
      <div class="row"><span class="name">50 WINGS</span><span class="dots"></span><span class="price">35.99</span></div>
      <div class="center">mild, hot, lemon pepper, sweet chili, teriyaki, garlic Parmesan</div>
    </div>

    <h2 class="tag" style="left:175px;top:608px;">BAR-B-QUE</h2>
    <div class="list" style="left:38px;top:651px;width:359px;">
      <div class="row"><span class="name">BABY BACK RIBS</span><span class="dots" style="border:0;"></span><span class="name">half rack - 12.99</span><span class="dots"></span><span class="price">full rack -18.99</span></div>
      <div class="row"><span class="name">- BRISKET BURGER</span><span class="dots"></span><span class="price">8.25</span></div>
      <div class="row"><span class="name">- BARBECUE COMBO</span><span class="dots"></span><span class="price">17.99</span></div>
      <div>- half rack of ribs, brisket, and sausage</div>
      <div>- served with potato salad and red beans.</div>
    </div>

    <p class="center" style="position:absolute;left:0;right:0;top:730px;font-family:'Raleway',sans-serif;font-weight:700;font-size:14px;line-height:28px;">
      ADD A <span style="font-size:25px;">15% GRATUITY</span> ON <span style="font-size:22px;">6</span><br>
      <span style="font-size:21px;">PERSONS</span> OR MORE...
    </p>
    <footer class="footer-band"><span style="font-size:26px;font-weight:700;">Call Us : 956-555-0148</span></footer>
  </section>

  <!-- Cover -->
  <section class="panel panel--cover">
    <div class="brand" style="position:absolute;left:0;right:0;top:150px;display:flex;align-items:center;justify-content:center;gap:12px;">
      <span style="width:26px;height:26px;border-radius:50%;background:var(--orange);"></span>
      <span style="font-family:'Fredoka',sans-serif;font-weight:600;font-size:58px;color:var(--orange);">Lurma's</span>
    </div>

    <svg style="position:absolute;left:0;top:300px;" width="433" height="210" viewBox="0 0 433 210" aria-hidden="true">
      <path d="M0 48 L433 8 L433 170 L0 200 Z" fill="var(--yellow)"/>
      <path d="M0 48 L433 8" stroke="#f9ef9a" stroke-width="2"/>
    </svg>
    <h1 style="position:absolute;left:30px;top:345px;width:400px;text-align:center;font-family:'Fredoka',sans-serif;font-weight:600;color:var(--dark);transform:rotate(-4deg);line-height:1;">
      <span style="display:block;font-size:42px;">Food and Drink</span>
      <span style="display:block;font-size:64px;margin-top:4px;">Menu</span>
    </h1>

    <div class="center" style="position:absolute;left:0;right:0;top:576px;font-family:'Raleway',sans-serif;color:#e8ddd0;">
      <p style="font-size:19px;line-height:24px;letter-spacing:.5px;">BREAKFAST, APPETIZERS,<br>BURGERS AND SANDWICHES</p>
      <p style="font-size:14px;font-weight:700;margin-top:10px;">SPECIALTIES</p>
      <p style="font-size:14.5px;line-height:19px;margin-top:4px;">SOUTH OF BORDER, COMBINATION PLATES,<br>SEAFOOD, SOUPS, FAMILY PLATTERS ... DRINKS</p>
    </div>

    <footer class="footer-band" style="height:90px;flex-direction:column;border-top:3px solid #e8ddd0;">
      <span style="font-size:16px;font-weight:700;">Call Us : 956-555-0148</span>
      <span style="font-size:15px;margin-top:3px;">718 N. CALLOWAY ST. ELSA TEXAS</span>
      <span style="font-size:15px;margin-top:3px;">www.lurmasrestaurant.com</span>
    </footer>
  </section>

</main>
</body>
</html>
```